Business card design needed

We are a Custom Joinery and specialise in design, Manufacture and Installation of kitchens and cabinetry
We currently have a logo based on the northern star in red and black but are open to something that would look fresh and clean
Updates

Project Deadline Extended
Reason: Need a couple days to go through designs. Finding some designs that are great on front and others great on reverse. I would like to be able to comment and get the total look we are after.

Target Market(s)

30-50 year olds who are looking to renovate

Industry/Entity Type

Business

Contact Information for Business Card

Larchfield Fitouts
ABN 37 418 260 573
Colin Pratley - Cabinetmaker/Designer Licence No. 318570K

Requirements
Nice to have
• Maybe a nice fresh modern kitchen picture

```html
<!DOCTYPE html>
<html lang="en">
<head>
<meta charset="utf-8">
<title>Larchfield Fitouts – Business Card</title>
<link href="https://fonts.googleapis.com/css2?family=Arimo:wght@400;700&display=swap" rel="stylesheet">
<style>
  :root {
    --canvas-bg: #1f1f1f;
    --card-dark: #333333;
    --card-light: #ffffff;
    --brand-red: #c8121b;
    --ink: #222222;
    --ink-soft: #555555;
    --white: #ffffff;
  }
  * { box-sizing: border-box; margin: 0; padding: 0; }
  html, body {
    width: 1200px; height: 900px; overflow: hidden;
    background: var(--canvas-bg);
    font-family: "Arimo", Arial, sans-serif;
  }
  .stage { position: relative; width: 1200px; height: 900px; }
  .card {
    position: absolute; top: 293px; width: 514px; height: 314px;
    box-shadow: 0 4px 14px rgba(0,0,0,.5);
    overflow: hidden;
  }
  /* Front */
  .card-front { left: 72px; background: var(--card-dark); }
  .front-mark {
    position: absolute; left: 120px; top: 98px;
    width: 62px; height: 62px; background: var(--brand-red);
  }
  .front-name {
    position: absolute; left: 212px; top: 70px;
    color: var(--white); font-size: 37px; line-height: 40px;
    letter-spacing: 1px; text-transform: uppercase; font-weight: 400;
  }
  .front-legal {
    position: absolute; right: 36px; top: 268px;
    color: var(--white); font-size: 10px; line-height: 12px; text-align: right;
  }
  /* Back */
  .card-back { left: 615px; background: var(--card-light); }
  .back-brand {
    position: absolute; left: 30px; top: 40px;
    display: flex; align-items: center; gap: 10px;
  }
  .back-mark { width: 26px; height: 26px; background: var(--brand-red); }
  .back-name {
    color: var(--ink-soft); font-size: 15px; line-height: 17px;
    text-transform: uppercase; letter-spacing: .5px;
  }
  .contact { position: absolute; left: 39px; top: 136px; color: var(--ink); }
  .person-name { color: var(--brand-red); font-size: 18px; line-height: 20px; }
  .person-role { font-size: 13px; line-height: 16px; }
  .address { margin-top: 12px; font-size: 13px; line-height: 16px; }
  .lines { margin-top: 10px; font-size: 13px; line-height: 16px; }
  .lines b { color: var(--brand-red); display: inline-block; width: 16px; }
  .photo {
    position: absolute; left: 253px; top: 0; width: 261px; height: 314px;
    border-left: 2px solid var(--brand-red);
    background: linear-gradient(180deg, #e9e9ea 0%, #d9d9db 30%, #b8141b 55%, #c7c7c9 78%, #9e1016 100%);
  }
</style>
</head>
<body>
<main class="stage">
  <section class="card card-front">
    <div class="front-mark"></div>
    <div class="front-name">Larchfield<br>Fitouts</div>
    <div class="front-legal">ABN 37 418 260 573<br>Licence No. 318570K</div>
  </section>

  <section class="card card-back">
    <div class="back-brand">
      <div class="back-mark"></div>
      <div class="back-name">Larchfield<br>Fitouts</div>
    </div>
    <div class="contact">
      <p class="person-name">Colin Pratley</p>
      <p class="person-role">Cabinetmaker/Designer</p>
      <p class="address">Unit 12<br>14-20 Kessel Rd<br>Emu Plains NSW 2750</p>
      <p class="lines">
        <b>M:</b> 0412 555 037<br>
        <b>F:</b> 9555 0184<br>
        <b>E:</b> hello@larchfieldfitouts.com.au
      </p>
    </div>
    <div class="photo" role="img" aria-label="Modern kitchen with red gloss cabinetry, stainless steel island and range hood"></div>
  </section>
</main>
</body>
</html>
```